Gym Wall Story Feature-- Long Horizontal design for the full-width of the gym wall

We need a horizontal, LONG, story poster/display that artfully tells our gym's story using ALL of the attached information and photographs. I've also included where this display will go in our gym (aligned with, and under the trophies.) Please incorporate the color scheme of white, light grey, dark grey, and orange.

Thanks!

Target Market(s)

Upscale, exclusive, hip gym community

Industry/Entity Type

Gym

Font styles to use
Sans Serif

Colors
ffffff
000000
aaaaaa
5c5c5c
f78f20
e9e9e9

Requirements
Must have
• All images and text provided in the attachments. Clean, modern, design. MOSTLY white with just a couple pops of orange and light grey. text should be black or charcoal and easy to read. We would like to have our logo incorporated as well.
Nice to have
• Clean, stream-line look, nothing too busy or crowded.
Should not have
• Too busy, slanted lines, weird fonts, misalignment.

```html
<!DOCTYPE html>
<html lang="en">
<head>
<meta charset="utf-8">
<title>The Groundwork – Our Story</title>
<link href="https://fonts.googleapis.com/css2?family=Open+Sans:ital,wght@0,400;0,600;0,700;0,800;1,600&display=swap" rel="stylesheet">
<style>
  :root{
    --white:#ffffff;
    --black:#000000;
    --charcoal:#3d3d3d;
    --mid-grey:#5c5c5c;
    --soft-grey:#aaaaaa;
    --light-grey:#e9e9e9;
    --orange:#f78f20;
    --orange-deep:#ee6a22;
  }
  *{box-sizing:border-box;margin:0;padding:0}
  html,body{width:1200px;height:168px;overflow:hidden;background:var(--white)}
  body{font-family:"Open Sans",Arial,sans-serif;color:var(--charcoal)}
  .story-wall{position:relative;width:1200px;height:168px;background:var(--white)}

  .brand{position:absolute;left:20px;top:58px;width:178px;display:flex;flex-direction:column;align-items:flex-start}
  .brand-row{display:flex;align-items:center;gap:6px}
  .brand-mark{width:10px;height:10px;background:var(--orange)}
  .brand-name{font-size:22px;font-weight:800;color:var(--mid-grey);letter-spacing:-.3px;line-height:1}
  .brand-tagline{margin-top:6px;font-size:9.5px;font-weight:700;color:var(--mid-grey);letter-spacing:1.6px}

  .era-photo{position:absolute;top:0;height:168px;overflow:hidden}
  .era-photo .photo-fill{position:absolute;inset:0}
  .era-year{position:absolute;left:0;right:0;bottom:0;height:26px;background:rgba(60,60,60,.92);
    color:var(--white);font-weight:700;font-size:19px;text-align:center;line-height:26px}
  .era-1973{left:208px;width:117px}
  .era-1973 .photo-fill{background:linear-gradient(160deg,#6e6e6e,#2a2a2a 70%,#8a8a8a)}
  .era-1981{left:488px;width:112px}
  .era-1981 .photo-fill{background:radial-gradient(ellipse at 50% 55%,#b0623a,#5a2c18 60%,#3a2418)}
  .era-2015{left:733px;width:113px}
  .era-2015 .photo-fill{background:linear-gradient(170deg,#d8d2b8,#8c8870 45%,#2e2e2e 80%)}

  .story-column{position:absolute;font-size:6.6px;line-height:8.6px;color:var(--charcoal);text-align:justify}
  .story-intro{left:340px;top:26px;width:138px}
  .story-title{font-size:14px;line-height:16px;font-weight:700;color:var(--orange-deep);text-align:left;margin-bottom:8px}
  .story-later{left:856px;top:8px;width:148px}
  .story-later p+p{margin-top:8.6px}

  .quote{position:absolute;left:608px;top:68px;width:112px;font-size:7.6px;line-height:9.6px;
    font-style:italic;font-weight:600;color:var(--orange-deep)}

  .titles-panel{position:absolute;left:1018px;top:22px;width:182px;height:124px;background:var(--white)}
  .titles-rule{position:absolute;left:1018px;top:22px;width:2px;height:124px;background:var(--light-grey)}
  .titles-head{position:absolute;left:1022px;top:30px;width:178px;height:18px;background:var(--orange-deep);
    color:var(--white);font-size:8.6px;font-weight:600;line-height:18px;padding-left:16px}
  .titles-list{position:absolute;left:1032px;top:56px;list-style:none}
  .titles-list li{display:flex;align-items:center;gap:7px;height:21px;font-size:9.4px;color:var(--charcoal)}
  .titles-list svg{width:12px;height:12px;flex:none}
</style>
</head>
<body>
<main class="story-wall">

  <div class="brand">
    <div class="brand-row"><span class="brand-mark"></span><span class="brand-name">THE GROUNDWORK</span></div>
    <span class="brand-tagline">PRIVATE TRAINING STUDIO</span>
  </div>

  <figure class="era-photo era-1973">
    <div class="photo-fill" role="img" aria-label="Black and white photo of the young founder posing shirtless with a competitor number"></div>
    <figcaption class="era-year">1973</figcaption>
  </figure>

  <section class="story-column story-intro">
    <h2 class="story-title">How Did<br>The Groundwork Start?</h2>
    <p>The Groundwork began with body builder and personal trainer, Harlan Reeve. Harlan had a passion for fitness early on and opened his first gym in 1960. Shortly after, Harlan won Mr. Tidewater. Harlan's body-building career looked promising until one evening he was robbed and shot in the chest. As a result, Harlan suffered from nerve damage in the arm and figured at the age of 34, his weight lifting days were over.</p>
  </section>

  <figure class="era-photo era-1981">
    <div class="photo-fill" role="img" aria-label="Colour photo of the founder flexing on stage in 1981"></div>
    <figcaption class="era-year">1981</figcaption>
  </figure>

  <blockquote class="quote">“I thought I was through and couldn't continue lifting but The Groundwork changed everything.”</blockquote>

  <figure class="era-photo era-2015">
    <div class="photo-fill" role="img" aria-label="Photo of the founder in a black training shirt inside the gym in 2015"></div>
    <figcaption class="era-year">2015</figcaption>
  </figure>

  <section class="story-column story-later">
    <p>Harlan started with 2-pound weights and changed his whole training technique. No more bouncing or slinging, just steady and controlled movements. Through hard work and consistency, Harlan started shaping up his upper-body again.</p>
    <p>Shortly after turning 40, Harlan won the National Mr. Continental competition.</p>
    <p>Through his experiences, Harlan created The Groundwork; a system that helps individuals develop a fundamentally sound workout regimen and accountability system.</p>
  </section>

  <div class="titles-panel"></div>
  <div class="titles-rule"></div>
  <div class="titles-head">National Championships Won</div>
  <ul class="titles-list">
    <li><svg viewBox="0 0 12 12" aria-hidden="true"><path fill="#ee6a22" d="M3 1h6v1h2.5v1.5c0 1.6-1.2 2.7-2.7 2.9A3.5 3.5 0 0 1 6.6 8v1.5H8.5V11h-5V9.5h1.9V8A3.5 3.5 0 0 1 3.2 6.4C1.7 6.2.5 5.1.5 3.5V2H3zM1.5 3v.5c0 1 .7 1.8 1.6 1.9A5 5 0 0 1 3 4V3zm9 0H9v1c0 .5 0 .9-.1 1.4.9-.1 1.6-.9 1.6-1.9z"/></svg>1981 Won Past 40 Mr. Continental</li>
    <li><svg viewBox="0 0 12 12" aria-hidden="true"><path fill="#ee6a22" d="M3 1h6v1h2.5v1.5c0 1.6-1.2 2.7-2.7 2.9A3.5 3.5 0 0 1 6.6 8v1.5H8.5V11h-5V9.5h1.9V8A3.5 3.5 0 0 1 3.2 6.4C1.7 6.2.5 5.1.5 3.5V2H3zM1.5 3v.5c0 1 .7 1.8 1.6 1.9A5 5 0 0 1 3 4V3zm9 0H9v1c0 .5 0 .9-.1 1.4.9-.1 1.6-.9 1.6-1.9z"/></svg>1996 Won Past 50 Mr. Continental</li>
    <li><svg viewBox="0 0 12 12" aria-hidden="true"><path fill="#ee6a22" d="M3 1h6v1h2.5v1.5c0 1.6-1.2 2.7-2.7 2.9A3.5 3.5 0 0 1 6.6 8v1.5H8.5V11h-5V9.5h1.9V8A3.5 3.5 0 0 1 3.2 6.4C1.7 6.2.5 5.1.5 3.5V2H3zM1.5 3v.5c0 1 .7 1.8 1.6 1.9A5 5 0 0 1 3 4V3zm9 0H9v1c0 .5 0 .9-.1 1.4.9-.1 1.6-.9 1.6-1.9z"/></svg>1999 Won Past 60 Mr. Continental</li>
    <li><svg viewBox="0 0 12 12" aria-hidden="true"><path fill="#ee6a22" d="M3 1h6v1h2.5v1.5c0 1.6-1.2 2.7-2.7 2.9A3.5 3.5 0 0 1 6.6 8v1.5H8.5V11h-5V9.5h1.9V8A3.5 3.5 0 0 1 3.2 6.4C1.7 6.2.5 5.1.5 3.5V2H3zM1.5 3v.5c0 1 .7 1.8 1.6 1.9A5 5 0 0 1 3 4V3zm9 0H9v1c0 .5 0 .9-.1 1.4.9-.1 1.6-.9 1.6-1.9z"/></svg>2009 Won Past 70 Mr. Continental</li>
  </ul>

</main>
</body>
</html>
```